QuartzNook Works, LLC Corporate Web Site

The goal of this web site is simple. To provide an information and corporate information site for people who click on company links from other web sites. Put simply, this web site is primarily a brochure web site for the parent business. It will contain information about the company and our products with links to those products. It will be designed as a small web site but scalable as we add more products and services to our repertoire.

Please see the PDF in the uploaded files/media for more information on colors and basic guidelines, but be creative for sure.

Target Market(s)

General

Industry/Entity Type

Technology, Software

Coding

Coded - Design and coding required

Font styles to use
Other font styles liked:
• Goliath, Roboto

Colors
FFC000
F8CF3A
FAE287
FDF2CF
FEFAEE

Requirements
Must have
• Home page template, interior template, News/Press release template
Nice to have
• Searchable
Should not have
• carousels, one-page design

```html
<!DOCTYPE html>
<html lang="en">
<head>
<meta charset="utf-8">
<title>QuartzNook Works — Web Site Layouts</title>
<link href="https://fonts.googleapis.com/css2?family=Poppins:wght@400;500;600;700&display=swap" rel="stylesheet">
<style>
:root{
  --stage:#9a9a9a;
  --label:#3a3a3c;
  --orange:#f7931e;
  --orange-deep:#f08a0c;
  --ink:#1f1f24;
  --muted:#3d3d44;
  --white:#ffffff;
  --mist:#f0eff1;
  --violet:#6a72bf;
  --night:#14171c;
  --hero:#1c2026;
  --field:#d8d8dc;
}
*{box-sizing:border-box;margin:0;padding:0}
html,body{width:1200px;height:2405px;overflow:hidden}
body{background:var(--stage);font-family:"Poppins",sans-serif;color:var(--ink);position:relative}
.abs{position:absolute}
.version-label{position:absolute;top:88px;font-size:31px;font-weight:500;color:var(--label);letter-spacing:.3px}
.frame{position:absolute;background:var(--white);overflow:hidden}
.frame--desktop{left:248px;top:177px;width:451px;height:1484px}
.frame--mobile{left:790px;top:177px;width:183px;height:2070px}

/* shared */
.brand{position:absolute;color:var(--orange);font-weight:700;white-space:nowrap;display:flex;align-items:center}
.brand-dot{display:inline-block;border-radius:50%;background:var(--orange)}
.btn{position:absolute;background:var(--orange);color:var(--white);font-weight:500;display:flex;align-items:center;justify-content:center;white-space:nowrap}
.btn--ghost{background:transparent;border:1px solid var(--white)}
.section-title{position:absolute;color:var(--orange);font-weight:700;white-space:nowrap}
.copy{position:absolute;color:var(--muted)}
.center{text-align:center}
.photo{position:absolute}
.icon{position:absolute;display:block}

/* desktop header */
.nav{position:absolute;left:178px;top:21px;display:flex;gap:8px;font-size:5.6px;font-weight:500;color:#222}
.nav .is-active{color:var(--orange);border-bottom:1px solid var(--orange)}
.hero{position:absolute;background:linear-gradient(160deg,#2a2f36 0%,#16191e 55%,#262a30 100%)}
.hero-title{position:absolute;left:0;right:0;color:var(--white);font-weight:700;text-align:center;line-height:1.3}
.hero-copy{position:absolute;color:#e9e9ec;text-align:center}

.tabs-item{position:absolute;font-weight:500;color:#2a2a30;white-space:nowrap}
.tab-pill{position:absolute;background:var(--orange);color:var(--white);font-weight:500;border-radius:6px;display:flex;align-items:center;justify-content:center;white-space:nowrap}
.feature-card{position:absolute;background:radial-gradient(circle at 60% 30%,#2f6fb0 0%,#163d7a 45%,#0b1d44 100%);color:var(--white)}
.feature-card h3{position:absolute;font-weight:700;letter-spacing:.2px}
.feature-card p{position:absolute;line-height:1.4}

.products{position:absolute;background:radial-gradient(ellipse at 50% 60%,#3a1f6e 0%,#1f1845 55%,#120f2c 100%)}
.product-card{position:absolute;background:var(--white);text-align:center}
.product-icon{position:absolute;left:50%;transform:translateX(-50%);border-radius:50%;background:var(--orange);display:flex;align-items:center;justify-content:center}
.product-card h4{position:absolute;left:0;right:0;color:var(--orange);font-weight:500}
.product-card p{position:absolute;color:#2a2a30}
.product-card .btn{border-radius:8px;left:50%;transform:translateX(-50%)}

.contact{position:absolute;background:var(--mist)}
.contact-line{position:absolute;display:flex;align-items:flex-start;color:#2a2a30}
.dot-social{position:absolute;border-radius:50%}
.field{position:absolute;background:var(--white);border:1px solid var(--field);color:#77777d}

.newsletter{position:absolute;background:var(--orange);border-radius:5px;color:var(--white)}
.newsletter h5{position:absolute;font-weight:500;white-space:nowrap}
.newsletter p{position:absolute;line-height:1.3}
.pill-input{position:absolute;background:var(--white);border-radius:20px;border:2px solid var(--white);color:#9a9a9f}
.pill-submit{position:absolute;background:var(--orange);color:var(--white);border-radius:20px;display:flex;align-items:center;justify-content:center}

.footer{position:absolute;background:var(--night);color:#dcdce0}
.footer h6{position:absolute;color:var(--orange);font-weight:500;white-space:nowrap}
.footer ul{position:absolute;list-style:none}
.footer p{position:absolute}
.scroll-top{position:absolute;border-radius:50%;background:var(--orange);display:flex;align-items:center;justify-content:center}
</style>
</head>
<body>

<svg width="0" height="0" style="position:absolute" aria-hidden="true">
  <symbol id="i-phone" viewBox="0 0 24 24"><path d="M6.6 10.8a15.1 15.1 0 0 0 6.6 6.6l2.2-2.2a1 1 0 0 1 1-.25 11.4 11.4 0 0 0 3.6.57 1 1 0 0 1 1 1V20a1 1 0 0 1-1 1A17 17 0 0 1 3 4a1 1 0 0 1 1-1h3.5a1 1 0 0 1 1 1c0 1.25.2 2.45.57 3.57a1 1 0 0 1-.25 1z" fill="#f7931e"/></symbol>
  <symbol id="i-mail" viewBox="0 0 24 24"><rect x="2" y="5" width="20" height="14" rx="1.5" fill="#f7931e"/><path d="M3 6.5l9 6.5 9-6.5" stroke="#fff" stroke-width="1.6" fill="none"/></symbol>
  <symbol id="i-pin" viewBox="0 0 24 24"><path d="M12 2a7 7 0 0 0-7 7c0 5.2 7 13 7 13s7-7.8 7-13a7 7 0 0 0-7-7z" fill="#f7931e"/><circle cx="12" cy="9" r="2.6" fill="#fff"/></symbol>
  <symbol id="i-monitor" viewBox="0 0 24 24"><rect x="3" y="4" width="18" height="12" rx="1" fill="none" stroke="#fff" stroke-width="1.8"/><path d="M9 20h6M12 16v4" stroke="#fff" stroke-width="1.8"/></symbol>
  <symbol id="i-globe" viewBox="0 0 24 24"><circle cx="12" cy="12" r="8.5" fill="none" stroke="#fff" stroke-width="1.6"/><ellipse cx="12" cy="12" rx="3.6" ry="8.5" fill="none" stroke="#fff" stroke-width="1.4"/><path d="M3.5 12h17M5 8h14M5 16h14" stroke="#fff" stroke-width="1.2"/></symbol>
  <symbol id="i-news" viewBox="0 0 24 24"><rect x="3" y="5" width="18" height="14" rx="1" fill="none" stroke="#fff" stroke-width="1.6"/><rect x="6" y="8" width="5" height="4" fill="#fff"/><path d="M13 9h5M13 12h5M6 15h12" stroke="#fff" stroke-width="1.4"/></symbol>
  <symbol id="i-up" viewBox="0 0 24 24"><path d="M6 15l6-6 6 6" stroke="#fff" stroke-width="2.4" fill="none" stroke-linecap="round"/></symbol>
</svg>

<h1 class="version-label" style="left:248px">Desktop Version</h1>
<h1 class="version-label" style="left:789px">Mobile Version</h1>

<!-- ================= DESKTOP ================= -->
<section class="frame frame--desktop">
  <header>
    <div class="brand" style="left:32px;top:16px;font-size:13px;gap:4px"><span class="brand-dot" style="width:7px;height:7px"></span>QuartzNook Works</div>
    <nav class="nav"><span class="is-active">HOME</span><span>ABOUT US</span><span>PRODUCTS</span><span>PROJECTS</span><span>CONTRIBUTIONS</span><span>NEWS</span><span>PRIVACY</span></nav>
  </header>

  <div class="hero" style="left:0;top:49px;width:451px;height:250px" role="img" aria-label="Dimmed photo of hands working on a laptop keyboard">
    <h2 class="hero-title" style="top:75px;font-size:14.5px">WELCOME TO<br>QUARTZNOOK.COM</h2>
    <p class="hero-copy" style="left:68px;width:314px;top:118px;font-size:7.6px;line-height:11px">Lorem ipsum dolor sit amet, consectetur adipiscing elit, sed do eiusmod tempor incididunt ut labore et dolore magna aliqua. quis ipsum suspendisse ultrices gravida. Risus commodo viverra maecenas accumsan lacus vel facilisis.</p>
    <div class="btn" style="left:160px;top:168px;width:59px;height:14px;font-size:7.5px">Read More</div>
    <div class="btn btn--ghost" style="left:231px;top:168px;width:82px;height:14px;font-size:7.5px">Current Projects</div>
  </div>

  <h2 class="section-title" style="left:35px;top:318px;font-size:16px">Current Projects</h2>
  <p class="copy" style="left:37px;top:353px;width:215px;font-size:7.4px;line-height:11px">Lorem ipsum dolor sit amet, consectetur adipiscing elit, sed do eiusmod tempor inci labore et dolore</p>

  <div class="tab-pill" style="left:34px;top:396px;width:98px;height:14px;font-size:7.2px">Artificial Intelligenece</div>
  <span class="abs" style="left:133px;top:426px;width:1.5px;height:56px;background:var(--orange)"></span>
  <span class="abs" style="left:133px;top:482px;width:1.5px;height:51px;background:var(--violet)"></span>
  <div class="tabs-item" style="left:38px;top:425px;font-size:7.4px">Extended Reality</div>
  <div class="tabs-item" style="left:38px;top:450px;font-size:7.4px">Data Visualization</div>
  <div class="tabs-item" style="left:38px;top:473px;font-size:7.4px">Artificial Intelligenece</div>
  <div class="tabs-item" style="left:38px;top:498px;font-size:7.4px">Current Projects</div>
  <div class="tabs-item" style="left:38px;top:524px;font-size:7.4px">Extended Reality</div>

  <div class="feature-card" style="left:162px;top:387px;width:256px;height:157px;border-radius:38px 0 38px 0" role="img" aria-label="Blue network-of-points technology artwork">
    <h3 style="left:18px;top:71px;font-size:8.6px">ARTIFICIAL INTELIGENCE</h3>
    <p style="left:18px;top:90px;width:160px;font-size:7.4px">Lorem ipsum dolor sit amet, consectetur adipiscing elit, sed do eiusmod tempor incididunt ut labore</p>
    <div class="btn" style="left:19px;top:130px;width:68px;height:17px;font-size:8px">READ MORE</div>
  </div>

  <span class="abs" style="left:38px;top:603px;width:174px;height:185px;background:var(--violet)"></span>
  <div class="photo" style="left:100px;top:624px;width:129px;height:139px;background:linear-gradient(170deg,#3d4a3a 0%,#1f2c48 45%,#2a4a8a 70%,#14182a 100%);border:1px solid #fff" role="img" aria-label="Photo of an open laptop on a table outdoors"></div>
  <h2 class="section-title" style="left:261px;top:604px;font-size:16px">About Us</h2>
  <p class="copy" style="left:259px;top:629px;width:162px;font-size:7.4px;line-height:11px">Lorem ipsum dolor sit amet, consectetur adipiscing elit, sed do eiusmod tempor incididunt ut labore et dolore magna aliqua. Quis ipsum suspendisse ultrices gravida. Risus commodo viverra maecenas facilisis.consectetur adipiscing elit, sed do eiusmod tempor et dolore magna aliqua. Quis ipsum suspendisse Risus commodo viverra maecenas facilisis.</p>
  <div class="btn" style="left:260px;top:765px;width:69px;height:18px;font-size:8.5px">READ MORE</div>

  <section class="products" style="left:0;top:813px;width:451px;height:253px" role="img" aria-label="Dark purple blurred code-screen background">
    <h2 class="abs" style="left:0;right:0;top:24px;text-align:center;color:#fff;font-size:14.5px;font-weight:600">Our Products</h2>
    <div class="product-card" style="left:33px;top:64px;width:117px;height:157px;border-radius:14px 0 26px 14px">
      <div class="product-icon" style="top:14px;width:32px;height:32px"><svg width="18" height="18"><use href="#i-globe"/></svg></div>
      <h4 style="top:53px;font-size:8.6px">NOOK SUITE</h4>
      <p style="left:14px;width:89px;top:70px;font-size:7.4px;line-height:11px">Lorem ipsum dolor sit amet, consectetur adipiscing elit, sed do eiusmod tempor</p>
      <div class="btn" style="top:123px;width:46px;height:11px;font-size:6.2px">Read More</div>
    </div>
    <div class="product-card" style="left:166px;top:64px;width:118px;height:157px;border-radius:14px 0 26px 14px">
      <div class="product-icon" style="top:11px;width:32px;height:32px"><svg width="17" height="17"><use href="#i-monitor"/></svg></div>
      <h4 style="top:53px;font-size:8.6px">NOOK SUITE</h4>
      <p style="left:14px;width:90px;top:70px;font-size:7.4px;line-height:11px">Lorem ipsum dolor sit amet, consectetur adipiscing elit, sed do eiusmod tempor</p>
      <div class="btn" style="top:123px;width:46px;height:11px;font-size:6.2px">Read More</div>
    </div>
    <div class="product-card" style="left:301px;top:64px;width:117px;height:157px;border-radius:14px 0 26px 14px">
      <div class="product-icon" style="top:11px;width:32px;height:32px"><svg width="17" height="17"><use href="#i-news"/></svg></div>
      <h4 style="top:53px;font-size:8.6px">NOOK SUITE</h4>
      <p style="left:14px;width:89px;top:70px;font-size:7.4px;line-height:11px">Lorem ipsum dolor sit amet, consectetur adipiscing elit, sed do eiusmod tempor</p>
      <div class="btn" style="top:123px;width:46px;height:11px;font-size:6.2px">Read More</div>
    </div>
  </section>

  <section class="contact" style="left:0;top:1066px;width:451px;height:217px">
    <h2 class="section-title" style="left:82px;top:37px;font-size:15.5px">Contact us</h2>
    <div class="contact-line" style="left:82px;top:67px;font-size:7px;gap:4px"><svg width="8" height="8"><use href="#i-phone"/></svg>555-010-2040</div>
    <div class="contact-line" style="left:82px;top:87px;font-size:7px;gap:4px"><svg width="9" height="8"><use href="#i-mail"/></svg>hello@quartznook.com</div>
    <div class="contact-line" style="left:82px;top:106px;font-size:7px;line-height:10px;gap:4px"><svg width="9" height="10"><use href="#i-pin"/></svg>Lorem ipsum dolor sit amet,<br>consectetur dolor sit amet</div>
    <span class="dot-social" style="left:84px;top:131px;width:12px;height:12px;background:#1d9bf0"></span>
    <span class="dot-social" style="left:100px;top:131px;width:12px;height:12px;background:#d6267a"></span>
    <span class="dot-social" style="left:116px;top:131px;width:12px;height:12px;background:#3b5998"></span>
    <div class="field" style="left:225px;top:41px;width:150px;height:16px;font-size:6.5px;padding:4px 6px">Enter your name</div>
    <div class="field" style="left:225px;top:67px;width:150px;height:16px;font-size:6.5px;padding:4px 6px">Enter your email</div>
    <div class="field" style="left:225px;top:91px;width:150px;height:35px;font-size:6.5px;padding:3px 6px">Message</div>
    <div class="btn" style="left:225px;top:134px;width:150px;height:17px;font-size:7.5px">Submit</div>
  </section>

  <footer class="footer" style="left:0;top:1283px;width:451px;height:201px">
    <h6 style="left:31px;top:50px;font-size:6.3px">About Us</h6>
    <p style="left:31px;top:70px;width:122px;font-size:5.6px;line-height:8.5px">Lorem Ipsum is simply dummy text of the printing and typesetting industry. Lorem Ipsum has been the industry's standard dummy text ever since the 1500s.</p>
    <h6 style="left:177px;top:49px;font-size:6.3px">Links</h6>
    <ul style="left:177px;top:65px;font-size:5.6px;line-height:11.2px"><li>About Us</li><li>Products</li><li>Projects</li><li>Contributions</li><li>News Privacy</li></ul>
    <h6 style="left:260px;top:49px;font-size:6.3px">Support</h6>
    <ul style="left:260px;top:65px;font-size:5.6px;line-height:11px"><li>FAQ</li><li>How it</li><li>Features</li><li>Contact</li><li>Reporting</li></ul>
    <h6 style="left:348px;top:50px;font-size:6.3px">Contact</h6>
    <div class="contact-line" style="left:348px;top:67px;font-size:5.4px;line-height:6.6px;gap:4px;color:#dcdce0"><svg width="7" height="7"><use href="#i-phone"/></svg>Phone Number<br>+015550199</div>
    <div class="contact-line" style="left:348px;top:89px;font-size:5.4px;line-height:6.6px;gap:4px;color:#dcdce0"><svg width="7" height="7"><use href="#i-mail"/></svg>Email Address<br>info@quartznook.com</div>
    <div class="contact-line" style="left:348px;top:111px;font-size:5.4px;line-height:6.6px;gap:4px;color:#dcdce0"><svg width="7" height="7"><use href="#i-pin"/></svg>Office Address<br>Your Address Is Here</div>
    <span class="abs" style="left:31px;top:154px;width:388px;height:1px;background:#4a4d55"></span>
    <div class="scroll-top" style="left:420px;top:142px;width:23px;height:23px"><svg width="12" height="12"><use href="#i-up"/></svg></div>
    <div class="brand" style="left:29px;top:165px;font-size:12.5px;gap:4px"><span class="brand-dot" style="width:7px;height:7px"></span>QuartzNook Works</div>
    <p style="left:180px;top:172px;font-size:5.6px">Copyright @2030. All Rights Reserved</p>
  </footer>

  <div class="newsletter" style="left:52px;top:1252px;width:358px;height:64px">
    <h5 style="left:23px;top:12px;font-size:11px">Newsletter Sign Up!</h5>
    <p style="left:23px;top:32px;width:130px;font-size:5.4px">Lorem ipsum dolor sit amet, consectetur adipiscing elit, sed do eiusmod tempor</p>
    <div class="pill-input" style="left:195px;top:22px;width:141px;height:22px;font-size:5.2px;padding:6px 8px">Email here</div>
    <div class="pill-submit" style="left:288px;top:25px;width:46px;height:16px;font-size:5.4px">SUBMIT</div>
  </div>
</section>

<!-- ================= MOBILE ================= -->
<section class="frame frame--mobile">
  <header>
    <div class="brand" style="left:18px;top:10px;font-size:9.5px;gap:3px"><span class="brand-dot" style="width:5px;height:5px"></span>QuartzNook Works</div>
    <span class="abs" style="left:158px;top:12px;width:11px;height:1.6px;background:#222;box-shadow:0 3.5px 0 #222,0 7px 0 #222"></span>
  </header>

  <div class="hero" style="left:0;top:31px;width:183px;height:103px" role="img" aria-label="Dimmed photo of hands working on a laptop keyboard">
    <h2 class="hero-title" style="top:15px;font-size:9.4px;line-height:12px">WELCOME TO<br>QUARTZNOOK.COM</h2>
    <p class="hero-copy" style="left:22px;width:139px;top:44px;font-size:4.6px;line-height:6px">Lorem ipsum dolor sit amet, consectetur adipiscing elit, sed do eiusmod tempor incididunt ut labore et dolore magna aliqua.</p>
    <div class="btn" style="left:45px;top:70px;width:38px;height:8px;font-size:4.4px">Read More</div>
    <div class="btn btn--ghost" style="left:89px;top:70px;width:51px;height:8px;font-size:4.4px">Current Projects</div>
  </div>

  <h2 class="section-title" style="left:0;right:0;text-align:center;top:141px;font-size:11px">Current Projects</h2>
  <p class="copy center" style="left:18px;width:147px;top:159px;font-size:4.8px;line-height:6px">Lorem ipsum dolor sit amet, consectetur adipiscing elit, sed do eiusmod tempor inci labore et dolore</p>
  <div class="tab-pill" style="left:15px;top:184px;width:73px;height:12px;font-size:4.8px;border-radius:6px">Artificial Intelligenece</div>
  <div class="tabs-item" style="left:21px;top:202px;font-size:4.8px">Extended Reality</div>
  <div class="tabs-item" style="left:21px;top:216px;font-size:4.8px">Data Visualization</div>
  <div class="tabs-item" style="left:99px;top:187px;font-size:4.8px">Current Projects</div>
  <div class="tabs-item" style="left:99px;top:202px;font-size:4.8px">Artificial Intelligence</div>
  <div class="tabs-item" style="left:99px;top:216px;font-size:4.8px">Extended Reality</div>
  <div class="feature-card" style="left:19px;top:241px;width:150px;height:92px;border-radius:22px 0 22px 0" role="img" aria-label="Blue network-of-points technology artwork">
    <h3 style="left:7px;top:36px;font-size:7px">ARTIFICIAL INTELIGENCE</h3>
    <p style="left:7px;top:48px;width:92px;font-size:4.8px;line-height:6px">Lorem ipsum dolor sit amet, consectetur adipiscing elit, sed do eiusmod tempor.</p>
    <div class="btn" style="left:7px;top:73px;width:36px;height:8px;font-size:4.6px">Read More</div>
  </div>

  <h2 class="section-title" style="left:0;right:0;text-align:center;top:350px;font-size:10.5px">About Us</h2>
  <span class="abs" style="left:26px;top:370px;width:99px;height:140px;background:var(--violet)"></span>
  <div class="photo" style="left:58px;top:385px;width:98px;height:106px;background:linear-gradient(170deg,#3d4a3a 0%,#1f2c48 45%,#2a4a8a 70%,#14182a 100%);border:1px solid #fff" role="img" aria-label="Photo of an open laptop on a table outdoors"></div>
  <p class="copy" style="left:27px;top:516px;width:130px;font-size:6px;line-height:9.5px">Lorem ipsum dolor sit amet, consectetur adipiscing elit, sed do eiusmod tempor incididunt ut labore et dolore magna aliqua. Quis ipsum suspendisse ultrices gravida. Risus commodo viverra maecenas facilisis.consectetur adipiscing elit, sed do eiusmod tempor et dolore magna aliqua. Quis ipsum suspendisse Risus commodo viverra maecenas facilisis.</p>
  <div class="btn" style="left:28px;top:629px;width:60px;height:15px;font-size:7.5px">Read More</div>

  <section class="products" style="left:0;top:659px;width:183px;height:629px" role="img" aria-label="Dark purple blurred code-screen background">
    <h2 class="abs" style="left:0;right:0;top:15px;text-align:center;color:#fff;font-size:10.5px;font-weight:600">Our Products</h2>
    <div class="product-card" style="left:29px;top:47px;width:128px;height:169px;border-radius:12px 0 26px 0">
      <div class="product-icon" style="top:15px;width:35px;height:35px"><svg width="19" height="19"><use href="#i-globe"/></svg></div>
      <h4 style="top:54px;font-size:9.2px">NOOK SUITE</h4>
      <p style="left:15px;width:98px;top:73px;font-size:8px;line-height:12px">Lorem ipsum dolor sit amet, consectetur adipiscing elit, sed do eiusmod tempor</p>
      <div class="btn" style="top:132px;width:52px;height:12px;font-size:7px">Read More</div>
    </div>
    <div class="product-card" style="left:29px;top:239px;width:128px;height:169px;border-radius:0 0 26px 0">
      <div class="product-icon" style="top:12px;width:35px;height:35px"><svg width="19" height="19"><use href="#i-monitor"/></svg></div>
      <h4 style="top:54px;font-size:9.2px">NOOK SUITE</h4>
      <p style="left:15px;width:98px;top:73px;font-size:8px;line-height:12px">Lorem ipsum dolor sit amet, consectetur adipiscing elit, sed do eiusmod tempor</p>
      <div class="btn" style="top:132px;width:52px;height:12px;font-size:7px">Read More</div>
    </div>
    <div class="product-card" style="left:29px;top:432px;width:128px;height:171px;border-radius:12px 0 26px 0">
      <div class="product-icon" style="top:12px;width:35px;height:35px"><svg width="19" height="19"><use href="#i-monitor"/></svg></div>
      <h4 style="top:54px;font-size:9.2px">NOOK SUITE</h4>
      <p style="left:15px;width:98px;top:73px;font-size:8px;line-height:12px">Lorem ipsum dolor sit amet, consectetur adipiscing elit, sed do eiusmod tempor</p>
      <div class="btn" style="top:134px;width:52px;height:12px;font-size:7px">Read More</div>
    </div>
  </section>

  <h2 class="section-title" style="left:20px;top:1304px;font-size:10.5px">Contact us</h2>
  <div class="contact-line" style="left:20px;top:1333px;font-size:7.5px;gap:5px"><svg width="9" height="9"><use href="#i-phone"/></svg>555-010-2040</div>
  <div class="contact-line" style="left:20px;top:1353px;font-size:7.5px;gap:5px"><svg width="10" height="9"><use href="#i-mail"/></svg>hello@quartznook.com</div>
  <div class="contact-line" style="left:20px;top:1372px;font-size:7.5px;line-height:11px;gap:5px"><svg width="10" height="11"><use href="#i-pin"/></svg>Lorem ipsum dolor sit amet,<br>consectetur dolor sit amet</div>
  <span class="dot-social" style="left:66px;top:1408px;width:13px;height:13px;background:#1d9bf0"></span>
  <span class="dot-social" style="left:84px;top:1408px;width:13px;height:13px;background:#d6267a"></span>
  <span class="dot-social" style="left:102px;top:1408px;width:13px;height:13px;background:#3b5998"></span>
  <div class="field" style="left:30px;top:1432px;width:125px;height:12px;font-size:4.6px;padding:2px 3px">Enter your name</div>
  <div class="field" style="left:30px;top:1450px;width:125px;height:12px;font-size:4.6px;padding:2px 3px">Enter your email</div>
  <div class="field" style="left:30px;top:1466px;width:125px;height:25px;font-size:4.6px;padding:2px 3px">Message</div>
  <div class="btn" style="left:30px;top:1497px;width:125px;height:12px;font-size:5px">Submit</div>

  <footer class="footer" style="left:0;top:1551px;width:183px;height:519px">
    <div class="brand" style="left:20px;top:66px;font-size:12.5px;gap:4px"><span class="brand-dot" style="width:7px;height:7px"></span>QuartzNook Works</div>
    <h6 style="left:20px;top:104px;font-size:8.4px">About Us</h6>
    <p style="left:20px;top:120px;width:150px;font-size:8px;line-height:11.6px">Lorem Ipsum is simply dummy text of the printing and typesetting industry. Lorem Ipsum has been the industry's standard dummy</p>
    <h6 style="left:20px;top:196px;font-size:8.4px">Links</h6>
    <ul style="left:20px;top:211px;font-size:7.6px;line-height:12.8px"><li>About Us</li><li>Products</li><li>Projects</li><li>Contributions</li><li>News Privacy</li></ul>
    <h6 style="left:20px;top:292px;font-size:8.4px">Support</h6>
    <ul style="left:20px;top:307px;font-size:7.6px;line-height:12.8px"><li>FAQ</li><li>How it</li><li>Features</li><li>Contact</li><li>Reporting</li></ul>
    <h6 style="left:20px;top:388px;font-size:8.4px">Contact</h6>
    <div class="contact-line" style="left:20px;top:404px;font-size:7.6px;line-height:11px;gap:3px;color:#dcdce0"><svg width="9" height="9"><use href="#i-phone"/></svg>Phone Number<br>+015550199</div>
    <div class="contact-line" style="left:20px;top:437px;font-size:7.6px;line-height:11px;gap:3px;color:#dcdce0"><svg width="9" height="9"><use href="#i-mail"/></svg>Email Address<br>info@quartznook.com</div>
    <div class="contact-line" style="left:20px;top:470px;font-size:7.6px;line-height:11px;gap:3px;color:#dcdce0"><svg width="9" height="9"><use href="#i-pin"/></svg>Office Address<br>Your Address Is Here</div>
    <p style="left:20px;top:504px;font-size:6.2px">Copyright @2030. All Rights Reserved</p>
    <div class="scroll-top" style="left:164px;top:497px;width:13px;height:13px"><svg width="8" height="8"><use href="#i-up"/></svg></div>
  </footer>

  <div class="newsletter" style="left:17px;top:1521px;width:149px;height:68px">
    <h5 style="left:0;right:0;text-align:center;top:9px;font-size:9.2px">Newsletter Sign Up!</h5>
    <p style="left:14px;width:121px;top:23px;font-size:5px;text-align:center">Lorem ipsum dolor sit amet, consectetur accumsan lacus vel facilisis.</p>
    <div class="pill-input" style="left:29px;top:41px;width:91px;height:15px;font-size:4.4px;padding:3px 6px">Email here</div>
    <div class="pill-submit" style="left:85px;top:43px;width:33px;height:11px;font-size:4.4px">SUBMIT</div>
  </div>
</section>

</body>
</html>
```